Book Cover Design for a Novella

This book is a whimsical book about random philosophical thoughts. The size of the book is 4X6 inches, about 140 pages long. I would like the background color to be maroon. The title of the book is The Lantern Keeper's Crooked Almanac of Days, and the author name is Delia Marwood. I would like the lettering to either be black or gold, in a font that looks like handwriting. From the lower left corner of the front cover, I would like there to be a gold-colored gardenia.
On the back cover, this is the book summary/description: “We are meant to share our hearts, not give them away. Vulnerability is not the act of placing your heart in someone else’s hands, saying, ‘Keep this safe for me.’ Vulnerability is wearing your heart on your sleeve, showing others your beauty, truths, and fears, and trusting that they will respect you.”
For the author's bio: Delia Marwood is a native of Boulder, Colorado. She enjoys spending time with her cats, eating pasta, and contemplating random things, such as banana spiders, sewage systems, and other huge things that scare her.
I would like all the writing on the back to be in a black, regular font.
I will upload the author's photo, which I would like to be put next to the bio, and I will also attach a rough sketch of what I'd like the cover to look like. Message me with any questions! Thanks.

```html
<!DOCTYPE html>
<html lang="en">
<head>
<meta charset="utf-8">
<title>The Lantern Keeper's Crooked Almanac of Days — Book Cover</title>
<link rel="stylesheet" href="https://fonts.googleapis.com/css2?family=EB+Garamond&family=Pinyon+Script&family=Cinzel&display=swap">
<style>
  :root {
    --maroon-deep: #2c1a17;
    --maroon: #5a2a22;
    --maroon-warm: #9a4630;
    --spine: #3a2621;
    --gold-light: #f3d98a;
    --gold: #d9b04a;
    --gold-dark: #a7782a;
    --plaque: #c9a03a;
    --olive: #a7b04e;
    --rust: #b4582e;
    --ink: #1a120c;
    --white: #f4eee4;
  }
  * { margin: 0; padding: 0; box-sizing: border-box; }
  html, body { width: 1200px; height: 872px; overflow: hidden; background: var(--maroon-deep); }
  .cover { position: relative; width: 1200px; height: 872px; display: flex; }

  /* Back cover */
  .back {
    position: relative; width: 580px; height: 872px;
    background:
      radial-gradient(ellipse 260px 200px at 300px 40px, rgba(230,195,90,.85), transparent 70%),
      radial-gradient(ellipse 240px 300px at 0px 560px, rgba(190,90,45,.9), transparent 70%),
      radial-gradient(ellipse 300px 260px at 120px 860px, rgba(175,185,80,.95), transparent 70%),
      radial-gradient(ellipse 220px 220px at 420px 560px, rgba(200,190,90,.8), transparent 70%),
      radial-gradient(ellipse 220px 260px at 520px 820px, rgba(160,80,50,.8), transparent 70%),
      linear-gradient(180deg, #4a2c1c 0%, #8a5a2c 40%, #a06a34 70%, #7a5a30 100%);
    font-family: "EB Garamond", Garamond, serif;
    color: var(--ink);
  }
  .blurb {
    position: absolute; left: 26px; top: 40px; width: 534px; height: 340px;
    background: linear-gradient(135deg, #b7922f 0%, #d8b548 45%, #c7a23c 100%);
    -webkit-mask: radial-gradient(circle 22px at 0 0, transparent 98%, #000) top left,
                  radial-gradient(circle 22px at 100% 0, transparent 98%, #000) top right,
                  radial-gradient(circle 22px at 0 100%, transparent 98%, #000) bottom left,
                  radial-gradient(circle 22px at 100% 100%, transparent 98%, #000) bottom right;
    -webkit-mask-size: 51% 51%; -webkit-mask-repeat: no-repeat;
    mask: radial-gradient(circle 22px at 0 0, transparent 98%, #000) top left,
          radial-gradient(circle 22px at 100% 0, transparent 98%, #000) top right,
          radial-gradient(circle 22px at 0 100%, transparent 98%, #000) bottom left,
          radial-gradient(circle 22px at 100% 100%, transparent 98%, #000) bottom right;
    mask-size: 51% 51%; mask-repeat: no-repeat;
    display: flex; align-items: center; justify-content: center;
    padding: 0 22px 30px;
  }
  .blurb p { font-size: 23px; line-height: 34px; text-align: center; }
  .bio { position: absolute; left: 40px; top: 456px; width: 490px; }
  .author-photo {
    float: left; width: 224px; height: 208px; margin: 0 26px 8px 0;
    background: linear-gradient(160deg, #8fa3b8 0%, #6e7f8c 45%, #3c3a38 100%);
    box-shadow: 2px 3px 4px rgba(0,0,0,.5);
    border: 1px solid #ddd;
  }
  .bio p { font-size: 23px; line-height: 34px; text-align: center; padding-top: 8px; }

  /* Spine */
  .spine {
    width: 40px; height: 872px; background: var(--spine);
    display: flex; flex-direction: column; align-items: center; justify-content: space-between;
    padding: 52px 0 44px;
  }
  .spine span {
    writing-mode: vertical-rl; font-family: "Cinzel", "Trajan Pro", serif;
    color: var(--white); font-size: 15.5px; letter-spacing: .5px; white-space: nowrap;
  }

  /* Front cover */
  .front {
    position: relative; width: 580px; height: 872px;
    background:
      radial-gradient(ellipse 360px 280px at 240px 700px, rgba(170,80,55,.9), transparent 75%),
      radial-gradient(ellipse 300px 300px at 400px 480px, rgba(110,50,40,.7), transparent 75%),
      linear-gradient(180deg, #3e2720 0%, #4c2c24 45%, #5a2d25 100%);
  }
  .title {
    position: absolute; top: 44px; left: 0; width: 580px; text-align: center;
    font-family: "Pinyon Script", cursive; font-weight: 400;
    font-size: 54px; line-height: 72px;
    background: linear-gradient(180deg, var(--gold-light), var(--gold) 55%, var(--gold-dark));
    -webkit-background-clip: text; background-clip: text; color: transparent;
    text-shadow: 1px 2px 2px rgba(0,0,0,.25);
  }
  .gardenia {
    position: absolute; left: 0; top: 324px; width: 452px; height: 468px;
    background:
      radial-gradient(circle 110px at 310px 110px, #e6a042 0%, #c9782e 55%, transparent 100%),
      radial-gradient(ellipse 240px 120px at 160px 330px, rgba(170,170,80,.55), transparent 75%);
  }
  .author {
    position: absolute; top: 792px; left: 0; width: 580px; text-align: center;
    font-family: "Pinyon Script", cursive; font-size: 38px; line-height: 50px;
    background: linear-gradient(180deg, var(--gold-light), var(--gold) 55%, var(--gold-dark));
    -webkit-background-clip: text; background-clip: text; color: transparent;
  }
</style>
</head>
<body>
<main class="cover">
  <section class="back">
    <div class="blurb">
      <p>We are meant to share our hearts, not give them away. Vulnerability is not the act of placing your heart in someone else’s hands, saying, ‘Keep this safe for me.’ Vulnerability is wearing your heart on your sleeve, showing others your beauty, truths, and fears, and trusting that they will respect you.</p>
    </div>
    <div class="bio">
      <div class="author-photo" role="img" aria-label="Author portrait photograph"></div>
      <p>Delia Marwood is a native of Boulder, Colorado. She enjoys spending time with her cats, eating pasta, and contemplating random things, such as banana spiders, sewage systems, and other huge things that scare her.</p>
    </div>
  </section>

  <section class="spine">
    <span>THE LANTERN KEEPER'S CROOKED ALMANAC OF DAYS</span>
    <span>DELIA MARWOOD</span>
  </section>

  <section class="front">
    <h1 class="title">The Lantern Keeper's<br>Crooked Almanac<br>of Days</h1>
    <div class="gardenia" role="img" aria-label="Golden gardenia illustration with curling stem rising from the lower left"></div>
    <p class="author">Delia Marwood</p>
  </section>
</main>
</body>
</html>
```